Cleaning services Business Card Design

I need a business card design for my Cleaning business. I would like perhaps emphasis on the company name, Muddle to Marvel. Maybe the Muddle would to dirty and the marvel would have sprinkles.

Industry/Entity Type

Business

Contact Information for Business Card

Muddle to Marvel Cleaning Services, Teodoro Perlas, Industrial, Commercial, & Residential 418-635-0247

```html
<!DOCTYPE html>
<html lang="en">
<head>
<meta charset="utf-8">
<title>Muddle to Marvel Cleaning Services – Business Card</title>
<link href="https://fonts.googleapis.com/css2?family=Arimo:wght@400;700&display=swap" rel="stylesheet">
<style>
  :root {
    --page-bg: #ecebe8;
    --card-bg: #ffffff;
    --blue-deep: #1677bd;
    --blue-light: #5fcbe9;
    --blue-text: #1d8fd2;
    --stripe-grey: #b3b4b6;
    --text-grey: #8e8f91;
    --dot-blue: #27a3dd;
  }
  * { margin: 0; padding: 0; box-sizing: border-box; }
  html, body {
    width: 1200px; height: 780px; overflow: hidden;
    background: var(--page-bg);
    font-family: "Arimo", Arial, sans-serif;
  }
  .card {
    position: absolute; left: 75px; top: 90px;
    width: 1050px; height: 600px;
    background: var(--card-bg);
    box-shadow: 0 10px 30px rgba(0,0,0,.18);
    overflow: hidden;
  }
  .card-wave { position: absolute; inset: 0; }
  .holder {
    position: absolute; right: 60px; top: 48px;
    text-align: right; color: #fff;
  }
  .holder-name { font-size: 44px; font-weight: 700; letter-spacing: 1px; }
  .holder-title { font-size: 26px; margin-top: 2px; }
  .brand {
    position: absolute; left: 70px; top: 300px;
    display: flex; align-items: center; gap: 22px;
  }
  .brand-mark {
    width: 110px; height: 110px;
    background: var(--stripe-grey);
  }
  .brand-name {
    font-size: 46px; font-weight: 700; color: var(--blue-text);
    text-transform: uppercase; letter-spacing: -0.5px; line-height: 1;
  }
  .brand-tagline {
    font-size: 27px; color: var(--text-grey);
    text-transform: uppercase; letter-spacing: 7px; margin-top: 8px;
  }
  .contacts {
    position: absolute; left: 220px; top: 448px;
    list-style: none; color: var(--text-grey); font-size: 27px;
  }
  .contacts li { display: flex; align-items: center; gap: 14px; height: 40px; }
  .contact-icon {
    width: 28px; height: 28px; border-radius: 6px;
    background: var(--dot-blue);
  }
  .services {
    position: absolute; right: 46px; top: 300px;
    list-style: none; color: var(--text-grey); font-size: 27px; text-align: right;
  }
  .services li { display: flex; justify-content: flex-end; align-items: center; gap: 16px; height: 38px; }
  .services li::after {
    content: ""; width: 12px; height: 12px; border-radius: 50%;
    background: var(--dot-blue);
  }
</style>
</head>
<body>
  <section class="card">
    <svg class="card-wave" viewBox="0 0 1050 600" width="1050" height="600" aria-hidden="true">
      <defs>
        <linearGradient id="bandGradient" x1="0" y1="0" x2="1" y2="0">
          <stop offset="0" stop-color="#1677bd"/>
          <stop offset="0.55" stop-color="#5fcbe9"/>
          <stop offset="1" stop-color="#1a86c9"/>
        </linearGradient>
      </defs>
      <path d="M0,0 H1050 V175 C880,185 760,215 620,265 C430,330 300,130 0,100 Z" fill="url(#bandGradient)"/>
      <path d="M0,100 C300,130 430,330 620,265 C760,215 880,185 1050,175" fill="none" stroke="var(--stripe-grey)" stroke-width="14"/>
    </svg>

    <header class="holder">
      <div class="holder-name">TEODORO PERLAS</div>
      <div class="holder-title">Managing Director</div>
    </header>

    <div class="brand">
      <div class="brand-mark" role="img" aria-label="Company emblem area"></div>
      <div>
        <div class="brand-name">Muddle to Marvel</div>
        <div class="brand-tagline">Cleaning Services</div>
      </div>
    </div>

    <ul class="contacts">
      <li>
        <svg class="contact-icon" viewBox="0 0 28 28" aria-hidden="true"><rect width="28" height="28" rx="6" fill="var(--dot-blue)"/><path d="M9 7 L12 7 L13 11 L11 12.5 C12 15 13 16 15.5 17 L17 15 L21 16 L21 19 C21 20 20 21 19 21 C12 20 8 16 7 9 C7 8 8 7 9 7 Z" fill="#fff"/></svg>
        418-635-0247
      </li>
      <li>
        <svg class="contact-icon" viewBox="0 0 28 28" aria-hidden="true"><rect width="28" height="28" rx="6" fill="var(--dot-blue)"/><rect x="6" y="8" width="16" height="12" fill="none" stroke="#fff" stroke-width="1.8"/><path d="M6 8 L14 15 L22 8" fill="none" stroke="#fff" stroke-width="1.8"/></svg>
        info@muddletomarvel.com
      </li>
      <li>
        <svg class="contact-icon" viewBox="0 0 28 28" aria-hidden="true"><rect width="28" height="28" rx="6" fill="var(--dot-blue)"/><circle cx="14" cy="14" r="8" fill="none" stroke="#fff" stroke-width="1.8"/><ellipse cx="14" cy="14" rx="3.5" ry="8" fill="none" stroke="#fff" stroke-width="1.5"/><path d="M6 14 H22" stroke="#fff" stroke-width="1.5"/></svg>
        www.muddletomarvel.com
      </li>
    </ul>

    <ul class="services">
      <li>Industrial</li>
      <li>Commercial</li>
      <li>&amp; Residential</li>
    </ul>
  </section>
</body>
</html>
```